2in1 Bartender & Sommelier needs a business card

I need a business card. I worked as a bartender in many places but I just finished a sommelier school and I would like a new business card. I like minimal design, natural materials and something what makes the people think :) I try to be creative in cocktail making, like little mixology, little twist on recipes... I like to travel and discover new places, cultures and of course interesting drinks and improve continously...live a little bit crazy life. And I like what I do...

Target Market(s)

restaurant/winebar managers, winemakers, other sommeliers and bartenders, people who work in food and beverage sector

Industry/Entity Type

Hospitality

Contact Information for Business Card

Réka Fodor
Bartender & Sommelier
Phone: (FR) +33 6 4720 3917
(HU) +36 70 518 6092

Font styles to use
Script

Requirements
Must have
• Some sign, I am a bartender and sommelier as well.
Nice to have
• black and white maybe with 1 or 2 extra color
Should not have
• very colourful, to many things on the card

```html
<!DOCTYPE html>
<html lang="en">
<head>
<meta charset="utf-8">
<title>Réka Fodor — Bartender &amp; Sommelier</title>
<link rel="stylesheet" href="https://fonts.googleapis.com/css2?family=Fondamento&family=PT+Sans&display=swap">
<style>
  :root {
    --backdrop: #3a3f48;
    --card: #1e1f26;
    --card-deep: #191a20;
    --stripe-edge: #55565e;
    --ink: #8c8c93;
    --ink-soft: #7a7a82;
    --icon-bg: #5a5b62;
    --icon-ink: #1e1f26;
  }
  * { box-sizing: border-box; margin: 0; padding: 0; }
  html, body {
    width: 1200px;
    height: 675px;
    overflow: hidden;
    background: var(--backdrop);
  }
  .canvas {
    position: relative;
    width: 1200px;
    height: 675px;
    display: flex;
    align-items: center;
    justify-content: center;
  }
  .business-card {
    position: relative;
    width: 980px;
    height: 560px;
    background: var(--card);
    overflow: hidden;
    box-shadow: 0 20px 50px rgba(0,0,0,.35);
  }
  .stripe-panel {
    position: absolute;
    left: 0;
    top: 0;
    width: 380px;
    height: 560px;
  }
  .pour-lines {
    position: absolute;
    right: 0;
    top: 250px;
    width: 300px;
    height: 70px;
  }
  .contact {
    position: absolute;
    right: 92px;
    top: 62px;
    text-align: right;
    font-family: "PT Sans", sans-serif;
    color: var(--ink);
    font-size: 26px;
    line-height: 1.3;
    letter-spacing: .3px;
  }
  .contact-icon {
    display: inline-block;
    width: 48px;
    height: 48px;
    border-radius: 8px;
    background: var(--icon-bg);
    margin: 0 38px 18px 0;
  }
  .contact-icon svg { display: block; width: 48px; height: 48px; }
  .identity {
    position: absolute;
    left: 410px;
    top: 180px;
  }
  .identity-mark {
    width: 100px;
    height: 100px;
    border-radius: 50%;
    background: radial-gradient(circle at 50% 40%, #6c6d74, #3b3c43);
    margin-left: 20px;
    margin-bottom: 14px;
  }
  .name {
    font-family: "Fondamento", cursive;
    color: var(--ink);
    font-size: 64px;
    line-height: 1;
    white-space: nowrap;
  }
  .role {
    font-family: "Fondamento", cursive;
    color: var(--ink-soft);
    font-size: 30px;
    margin: 10px 0 0 40px;
    white-space: nowrap;
  }
</style>
</head>
<body>
<main class="canvas">
  <section class="business-card">
    <svg class="stripe-panel" viewBox="0 0 380 560" aria-hidden="true">
      <rect x="0" y="0" width="60" height="560" fill="#1b1c22"/>
      <rect x="60" y="0" width="70" height="560" fill="#202128"/>
      <rect x="130" y="0" width="70" height="560" fill="#1c1d23"/>
      <rect x="200" y="0" width="75" height="560" fill="#22232a"/>
      <rect x="275" y="0" width="105" height="560" fill="#1d1e25"/>
      <g stroke="var(--stripe-edge)" stroke-width="1.5">
        <line x1="60" y1="0" x2="60" y2="560"/>
        <line x1="130" y1="0" x2="130" y2="560"/>
        <line x1="200" y1="0" x2="200" y2="560"/>
        <line x1="275" y1="0" x2="275" y2="560"/>
        <line x1="380" y1="0" x2="380" y2="560" stroke-opacity=".6"/>
      </g>
    </svg>

    <svg class="pour-lines" viewBox="0 0 300 70" aria-hidden="true">
      <defs>
        <linearGradient id="line-fade" x1="0" x2="1">
          <stop offset="0" stop-color="#55565e" stop-opacity="0"/>
          <stop offset="1" stop-color="#55565e" stop-opacity="1"/>
        </linearGradient>
      </defs>
      <g stroke="url(#line-fade)" stroke-width="1.2">
        <line x1="0" y1="8" x2="300" y2="8"/>
        <line x1="20" y1="22" x2="300" y2="22"/>
        <line x1="40" y1="36" x2="300" y2="36"/>
        <line x1="60" y1="50" x2="300" y2="50"/>
        <line x1="80" y1="64" x2="300" y2="64"/>
      </g>
    </svg>

    <div class="contact">
      <span class="contact-icon">
        <svg viewBox="0 0 48 48" aria-label="Phone">
          <path d="M10 20c0-5 6-8 14-8s14 3 14 8v3h-7v-3c0-1-3-2-7-2s-7 1-7 2v3h-7z" fill="var(--icon-ink)"/>
          <path d="M15 24h18l3 13H12z" fill="var(--icon-ink)"/>
          <circle cx="24" cy="30" r="3.5" fill="var(--icon-bg)"/>
        </svg>
      </span>
      <p class="phone">(FR) +33 6 4720 3917</p>
      <p class="phone">(HU) +36 70 518 6092</p>
    </div>

    <div class="identity">
      <div class="identity-mark"></div>
      <h1 class="name">Réka Fodor</h1>
      <p class="role">Bartender &amp; Sommelier</p>
    </div>
  </section>
</main>
</body>
</html>
```